New Wrestling company needs a website

We need a website design for a new wrestling company in Australia that will be running 3-4 events per year. Wrestling company is Coralline Elite Grappling (CEG).

The design of the logo is in place and can be provided, and I have purchased the website domain.

A detailed description of the intent and purpose of this company can be provided.

The aim would be to have around 5 specific pages on CEG, with two standard “about” and “contact” pages. E.g.
- About CEG (focus and purpose of the company)
- CEG Events (specific focus on events run by CEG)
- CEG News (news and stories on wrestling’s across Oceania)
- CEG Media (where to watch CEG and our partners))
- CEG Partners and Sponsors (partner and affiliate information)
- CEG Power Rankings (top 10 ranked wrestlers from Oceania which is updated weekly)
- CEG fans (highlighting how to become part of CEG as a fan)
- Contact CEG
Updates

The logo design should now be included in the brief, please feel free to reach out to me directly if you can't access it or require any other information.

Target Market(s)

Wrestling Fans

Industry/Entity Type

Sport / Wrestling

Coding

Coded - Design and coding required

Number of Pages Required

5+ page

Requirements
Must have
• A Wrestling and or Sports feel to the website design

```html
<!DOCTYPE html>
<html lang="en">
<head>
<meta charset="utf-8">
<title>Coralline Elite Grappling</title>
<link href="https://fonts.googleapis.com/css2?family=Montserrat:wght@400;500;600;700;800&family=Roboto:wght@400;500;700&display=swap" rel="stylesheet">
<style>
:root{
  --blue:#2a9be0;
  --blue-dark:#1d86c8;
  --ink:#1b1b1b;
  --text:#555a60;
  --grey-bg:#eef0f3;
  --footer:#121212;
  --white:#ffffff;
}
*{box-sizing:border-box;margin:0;padding:0}
html,body{width:1200px;height:3950px;overflow:hidden}
body{font-family:"Montserrat",sans-serif;color:var(--ink);background:var(--white);position:relative}
.abs{position:absolute}

/* header */
.topbar{position:absolute;left:0;top:0;width:1200px;height:104px;background:var(--white);border-top:4px solid var(--blue)}
.brand{position:absolute;left:112px;top:34px;display:flex;align-items:center;gap:10px;font-weight:800;font-size:30px;color:var(--blue);letter-spacing:1px}
.brand-dot{width:16px;height:16px;border-radius:50%;background:var(--blue)}
.socials{position:absolute;left:562px;top:39px;display:flex;gap:7px}
.socials span{width:27px;height:27px;border-radius:50%;display:block}
.lang{position:absolute;left:725px;top:44px;font-family:"Roboto",sans-serif;font-size:13px;font-weight:500;display:flex;align-items:center;gap:6px}
.lang i{width:26px;height:18px;border-radius:3px;background:linear-gradient(var(--ink),var(--ink));background:#d9dde4;display:block;border:1px solid #c5cad2}
.callbox{position:absolute;left:820px;top:-4px;width:380px;height:108px;background:var(--blue);clip-path:polygon(28px 0,100% 0,100% 100%,0 100%)}
.callbox svg{position:absolute;left:66px;top:30px}
.callbox .lbl{position:absolute;left:106px;top:30px;color:var(--white);font-size:14px;font-weight:600}
.callbox .num{position:absolute;left:106px;top:50px;color:var(--white);font-size:21px;font-weight:700}

.nav{position:absolute;left:0;top:104px;width:1200px;height:49px;background:linear-gradient(#151515,#2a2a2a);display:flex;padding-left:149px}
.nav a{font-family:"Roboto",sans-serif;color:var(--white);font-size:13.5px;font-weight:700;text-decoration:none;line-height:49px;padding:0 14px}
.nav a.active{background:var(--blue);padding:0 15px}

/* hero */
.hero{position:absolute;left:0;top:153px;width:1200px;height:600px;background:#030303}
.hero-photo{position:absolute;left:560px;top:110px;width:640px;height:490px;background:radial-gradient(ellipse at 60% 45%,#7c1f2a 0%,#2a2f55 35%,#0b0d1a 65%,#030303 80%)}
.hero h1{position:absolute;left:112px;top:164px;color:var(--white);font-size:46px;font-weight:800;line-height:48px;letter-spacing:.5px}
.btn{display:inline-block;background:var(--blue);color:var(--white);font-family:"Roboto",sans-serif;font-weight:700;font-size:13px;border-radius:24px;text-align:center}
.hero .btn{position:absolute;left:112px;top:325px;width:141px;height:44px;line-height:44px}
.dots{position:absolute;left:111px;top:524px;display:flex;gap:5px}
.dots span{width:11px;height:11px;border-radius:50%;background:var(--white)}
.dots span:first-child{background:var(--blue)}

/* news */
.news-band{position:absolute;left:0;top:753px;width:1200px;height:256px;background:var(--blue)}
.sec-title-light{position:absolute;left:0;top:818px;width:1200px;text-align:center;color:var(--white);font-size:33px;font-weight:700}
.card{position:absolute;width:308px;height:455px;background:var(--white);box-shadow:0 2px 10px rgba(0,0,0,.15);padding:6px}
.card .ph{height:187px}
.card .meta{margin:22px 0 0 22px;font-family:"Roboto",sans-serif;font-size:12px;color:var(--ink);display:flex;align-items:center;gap:6px}
.card .meta b{width:12px;height:11px;border:2px solid var(--blue);border-radius:2px;display:block}
.card .meta em{width:12px;height:10px;background:var(--blue);border-radius:50%;display:block;margin-left:14px}
.card h3{margin:14px 0 0 22px;font-size:21px;font-weight:600}
.card p{margin:14px 22px 0 22px;font-size:13px;line-height:21px;color:var(--text)}
.card hr{margin:18px 22px 0 22px;border:none;border-top:1px solid #cfd3d8}
.card .btn{margin:22px 0 0 24px;width:141px;height:43px;line-height:43px;font-size:12.5px}

/* section tabs */
.tab{position:absolute;left:112px;width:394px;height:73px;background:var(--blue);color:var(--white);font-size:33px;font-weight:800;text-align:center;line-height:73px}
.rule{position:absolute;left:0;width:1200px;border-top:2px solid var(--blue)}

/* events */
.events{position:absolute;left:0;top:1944px;width:1200px;height:687px;background:var(--grey-bg)}
.tile{position:absolute;overflow:hidden}
.tile .date{position:absolute;left:32px;top:26px;width:50px;height:50px;border-radius:50%;background:var(--blue);color:var(--white);font-family:"Roboto",sans-serif;font-weight:700;font-size:15px;text-align:center;line-height:19px;padding-top:6px}
.tile .tt{position:absolute;left:100px;top:32px;color:var(--white);font-family:"Roboto",sans-serif;font-size:26px;white-space:nowrap}

/* who */
.who p{position:absolute;left:112px;top:2744px;width:471px;font-size:15px;line-height:21.5px;color:var(--text);text-align:justify}
.who .btn{position:absolute;left:112px;top:3006px;width:141px;height:44px;line-height:44px}
.who-frame{position:absolute;left:722px;top:2690px;width:324px;height:407px;border:11px solid var(--blue)}
.who-art{position:absolute;left:640px;top:2740px;width:470px;height:360px;background:radial-gradient(ellipse at 50% 50%,#d8343f 0%,#f0a56d 30%,#4d8fd6 55%,rgba(255,255,255,0) 72%)}

/* partners */
.logo-box{position:absolute;width:185px;height:86px;background:var(--white);box-shadow:0 1px 8px rgba(0,0,0,.15);display:flex;align-items:center;justify-content:center}
.logo-box span{display:block;width:54px;height:54px;border-radius:50%;background:#c9ced6}
.logo-box span.sq{border-radius:6px}

/* footer */
.footer{position:absolute;left:0;top:3557px;width:1200px;height:393px;background:var(--footer);color:var(--white)}
.fcol{position:absolute;top:108px}
.fcol h4{font-family:"Roboto",sans-serif;font-weight:400;font-size:27px}
.fcol ul{list-style:none;margin-top:22px}
.fcol li{font-family:"Roboto",sans-serif;font-size:14px;line-height:26px;padding-left:26px;position:relative}
.fcol.links li::before{content:"›";position:absolute;left:0;top:-1px;font-size:17px}
.fcol li svg{position:absolute;left:0;top:7px}
.copy{position:absolute;left:0;top:3878px;width:1200px;text-align:center;color:var(--white);font-family:"Roboto",sans-serif;font-size:13.5px}
</style>
</head>
<body>

<header class="topbar">
  <div class="brand"><span class="brand-dot"></span>CEG</div>
  <div class="socials">
    <span style="background:#3b5aa0"></span><span style="background:#2aa3e0"></span><span style="background:#e0413a"></span>
  </div>
  <div class="lang">Eng ⌄ <i></i></div>
  <div class="callbox">
    <svg width="36" height="36" viewBox="0 0 36 36" fill="none" stroke="#fff" stroke-width="2.5"><circle cx="18" cy="18" r="16"/><path d="M12 10l4 4-2 3c1.5 3 3 4.5 5 5l3-2 4 4-3 3c-6 0-14-8-14-14z" fill="#fff" stroke="none"/></svg>
    <div class="lbl">Call us Today :</div>
    <div class="num">+61 400 555 0192</div>
  </div>
</header>

<nav class="nav">
  <a class="active">HOME</a><a>ABOUT</a><a>EVENTS</a><a>NEWS</a><a>MEDIA</a><a>PARTNERS AND SPONSORS</a><a>POWER RANKINGS</a><a>FANS</a><a>CONTACT</a>
</nav>

<section class="hero">
  <div class="hero-photo" role="img" aria-label="Two wrestlers grappling on a blue mat under a spotlight"></div>
  <h1>WE ARE A NEW<br>WRESTLING COMPANY<br>IN AUSTRALIA</h1>
  <span class="btn">GET STARTED</span>
  <div class="dots"><span></span><span></span><span></span><span></span></div>
</section>

<div class="news-band"></div>
<h2 class="sec-title-light">CEG NEWS</h2>

<article class="card" style="left:112px;top:895px"><div class="ph" role="img" aria-label="Wrestlers in red on a mat" style="background:linear-gradient(135deg,#c8452f,#e07a50 50,#b33a3a)"></div><div class="meta"><b></b>Jan 20,2022<em></em></div><h3>Lorem ipsum dolor</h3><p>Lorem ipsum dolor sit amet, conse ctetur adipiscing elit, sed do eiusmo d tempor incididunt ut</p><hr><span class="btn">LEARN MORE ➜</span></article>
<article class="card" style="left:446px;top:895px"><div class="ph" role="img" aria-label="Wrestlers in red and blue grappling on a blue mat" style="background:linear-gradient(135deg,#3a4fae,#6b75c9 55%,#a8323b)"></div><div class="meta"><b></b>Jan 20,2022<em></em></div><h3>Lorem ipsum dolor</h3><p>Lorem ipsum dolor sit amet, conse ctetur adipiscing elit, sed do eiusmo d tempor incididunt ut</p><hr><span class="btn">LEARN MORE ➜</span></article>
<article class="card" style="left:780px;top:895px"><div class="ph" role="img" aria-label="Wrestlers competing on a red mat in a gym" style="background:linear-gradient(180deg,#6f7378,#c7494f 60%,#b8b0ac)"></div><div class="meta"><b></b>Jan 20,2022<em></em></div><h3>Lorem ipsum dolor</h3><p>Lorem ipsum dolor sit amet, conse ctetur adipiscing elit, sed do eiusmo d tempor incididunt ut</p><hr><span class="btn">LEARN MORE ➜</span></article>
<article class="card" style="left:112px;top:1387px"><div class="ph" role="img" aria-label="Two wrestlers on a dark stage" style="background:radial-gradient(ellipse at 50% 55%,#a6343c,#1b2a5a 45%,#050505 75%)"></div><div class="meta"><b></b>Jan 20,2022<em></em></div><h3>Lorem ipsum dolor</h3><p>Lorem ipsum dolor sit amet, conse ctetur adipiscing elit, sed do eiusmo d tempor incididunt ut</p><hr><span class="btn">LEARN MORE ➜</span></article>
<article class="card" style="left:446px;top:1387px"><div class="ph" role="img" aria-label="Empty wrestling ring under stage lights" style="background:linear-gradient(180deg,#0b0b14,#3b2a66 55%,#0a0a12)"></div><div class="meta"><b></b>Jan 20,2022<em></em></div><h3>Lorem ipsum dolor</h3><p>Lorem ipsum dolor sit amet, conse ctetur adipiscing elit, sed do eiusmo d tempor incididunt ut</p><hr><span class="btn">LEARN MORE ➜</span></article>
<article class="card" style="left:780px;top:1387px"><div class="ph" role="img" aria-label="Packed arena around a lit ring" style="background:radial-gradient(ellipse at 50% 60%,#b7c3d4,#3b4251 40%,#101216 80%)"></div><div class="meta"><b></b>Jan 20,2022<em></em></div><h3>Lorem ipsum dolor</h3><p>Lorem ipsum dolor sit amet, conse ctetur adipiscing elit, sed do eiusmo d tempor incididunt ut</p><hr><span class="btn">LEARN MORE ➜</span></article>

<section class="events">
  <div class="rule" style="top:0"></div>
</section>
<div class="tab" style="top:1944px">CEG EVENTS</div>
<div class="tile" style="left:112px;top:2068px;width:440px;height:459px;background:radial-gradient(ellipse at 50% 65%,#7a3440,#1f2a5c 40%,#050505 72%)" role="img" aria-label="Two wrestlers locked together on a blue mat"><div class="date">Jan<br>10</div><div class="tt">Lorem ipsum dolor</div></div>
<div class="tile" style="left:573px;top:2068px;width:246px;height:218px;background:linear-gradient(160deg,#3b4d78,#8a6b70 50%,#4b6fa8)" role="img" aria-label="Wrestlers grappling in a hall"><div class="date">Jan<br>10</div><div class="tt" style="left:92px">Lorem ips</div></div>
<div class="tile" style="left:573px;top:2310px;width:246px;height:217px;background:linear-gradient(160deg,#0d1d3a,#b8323a 55%,#2f57a8)" role="img" aria-label="Wrestlers in red grappling"><div class="date">Jan<br>10</div><div class="tt" style="left:92px">Lorem ips</div></div>
<div class="tile" style="left:840px;top:2068px;width:247px;height:459px;background:linear-gradient(180deg,#2c4d8c,#3c4f7a 45%,#243a6a)" role="img" aria-label="Wrestler pinning opponent on a blue mat"><div class="date">Jan<br>10</div><div class="tt" style="left:94px">Lorem ips</div></div>

<div class="rule" style="top:2631px"></div>
<div class="tab" style="top:2631px">WHO WE ARE</div>
<section class="who">
  <p>Lorem ipsum dolor sit amet, consectetur adipiscing elit, sed do eiusmod tempor incididunt ut labore et dolore magna aliqua. Ut enim ad minim veniam, quis nostrud exercitation ullamco labori s nisi ut aliquip ex ea commodo consequat. Duis aute irure dolor in reprehenderit in voluptate velit esse cillum dolore eu fugiat nulla pariatur. Excepteur sint occaecat cupidatat non proident, sunt in culpa qui officia deserunt mollit anim id est laborum.Lo rem ipsum dolor sit amet, consectetur adipiscing elit, sed do eiusmod tempor incididunt ut labore et dolore magna aliqua. Ut enim ad minim veniam, quis nostrud exercitation ullamco laboris nisi ut aliquip ex ea commodo consequat.</p>
  <span class="btn">LEARN MORE</span>
  <div class="who-frame"></div>
  <div class="who-art" role="img" aria-label="Painted illustration of two wrestlers in red and blue singlets"></div>
</section>

<div class="rule" style="top:3154px"></div>
<div class="tab" style="top:3154px">OUR PARTNERS</div>
<div class="logo-box" style="left:112px;top:3265px"><span></span></div>
<div class="logo-box" style="left:310px;top:3265px"><span class="sq"></span></div>
<div class="logo-box" style="left:507px;top:3265px"><span></span></div>
<div class="logo-box" style="left:705px;top:3265px"><span class="sq"></span></div>
<div class="logo-box" style="left:903px;top:3265px"><span></span></div>
<div class="logo-box" style="left:112px;top:3370px"><span class="sq"></span></div>
<div class="logo-box" style="left:310px;top:3370px"><span></span></div>
<div class="logo-box" style="left:507px;top:3370px"><span class="sq"></span></div>
<div class="logo-box" style="left:705px;top:3370px"><span></span></div>
<div class="logo-box" style="left:903px;top:3370px"><span class="sq"></span></div>

<footer class="footer">
  <div class="fcol links" style="left:161px"><h4>Quick links</h4><ul><li>Home</li><li>About CEG</li><li>CEG Events</li><li>CEG News</li></ul></div>
  <div class="fcol links" style="left:306px;top:157px"><ul><li>CEG Media</li><li>Partners and Sponsors</li><li>Power Rankings</li><li>CEG fans</li></ul></div>
  <div class="fcol links" style="left:547px"><h4>Information</h4><ul><li>Contact us</li><li>About us</li><li>Privacy policy</li><li>Terms &amp; Conditions</li></ul></div>
  <div class="fcol" style="left:796px"><h4>Contact us</h4><ul>
    <li><svg width="13" height="13" viewBox="0 0 13 13"><path d="M2 1l3 3-1.5 2c1 2 2 3 3.5 3.5L9 8l3 3-2 2C5 13 0 8 0 3z" fill="#fff"/></svg>Phone : +61 400 555 0192</li>
    <li><svg width="13" height="11" viewBox="0 0 13 11"><rect width="13" height="11" rx="1" fill="#fff"/><path d="M0 1l6.5 5L13 1" stroke="#121212" fill="none"/></svg>Email : hello@corallinegrappling.au</li>
    <li><svg width="11" height="14" viewBox="0 0 11 14"><path d="M5.5 0A5.5 5.5 0 0 0 0 5.5C0 9 5.5 14 5.5 14S11 9 11 5.5A5.5 5.5 0 0 0 5.5 0z" fill="#fff"/><circle cx="5.5" cy="5.5" r="2" fill="#121212"/></svg>Address :</li>
    <li>Lorem ipsum dolor sit amet</li></ul></div>
</footer>
<div class="copy">© Copyright @2022 Coralline Elite Grappling | All Rights Reserved</div>

</body>
</html>
```